Eyebrow Tattooist business card design

I am an eyebrow specialist. I wax, shape, tint and tattoo eyebrows. I want a professional but classy image. I like gold raised writing on it. Colour of card either chocolate brown or pale blue??
As I use a technique called feathering and hair strokes, I would like the shape of a eyebrow on the front, with the hair strokes.

Industry/Entity Type
Tattoo
Contact Information for Business Card
I am an eyebrow specialist.
FRONT -  I want the name 'Glint Lashline' on the front of the card. With a shape of a brow, with every hair stroke. Need the words 'Tessa brow specialist and cosmetic tattooist' 'using feathered and hairstroke techniques'
03 5126-4730
BACK - At, Serene Glow Spa & Skin Studio. Shop 42, Hollin Park Market Arcade, Tamsworth-Delby Parade. Kelford Downs. Vic 3917.
www.glintlashline.com.au

```html
<!DOCTYPE html>
<html lang="en">
<head>
<meta charset="utf-8">
<title>Glint Lashline — Business Card</title>
<link rel="stylesheet" href="https://fonts.googleapis.com/css2?family=EB+Garamond:wght@400;600;700&display=swap">
<style>
  :root {
    --backdrop: #e9e4dc;
    --choc: #7a3a1e;
    --choc-light: #8e4524;
    --choc-dark: #5e2a15;
    --gold: #d8b23c;
    --gold-light: #f2d774;
    --gold-print: #dcbc1c;
    --paper: #f6f6f4;
  }
  * { box-sizing: border-box; margin: 0; padding: 0; }
  html, body {
    width: 1200px; height: 1000px; overflow: hidden;
    background: var(--backdrop);
    font-family: "EB Garamond", Georgia, serif;
  }
  .canvas { position: relative; width: 1200px; height: 1000px; }

  .card {
    position: absolute; left: 324px; width: 544px; height: 318px;
    box-shadow: 0 6px 18px rgba(60, 35, 20, 0.28);
    overflow: hidden;
  }
  .card-front {
    top: 220px;
    background: radial-gradient(ellipse at 55% 35%, var(--choc-light) 0%, var(--choc) 55%, var(--choc-dark) 100%);
    text-align: center; color: var(--gold);
  }
  .brow-art {
    position: absolute;
    background: linear-gradient(100deg, var(--gold) 0%, var(--gold-light) 55%, rgba(216,178,60,0.6) 100%);
    border-radius: 100% 100% 20% 40% / 100% 100% 10% 30%;
  }
  .card-front .brow-art { left: 118px; top: 58px; width: 306px; height: 100px; transform: rotate(-6deg); }
  .front-name {
    position: absolute; left: 0; right: 0; top: 168px;
    font-size: 56px; font-weight: 700; line-height: 1; letter-spacing: 0.5px;
    color: var(--gold);
  }
  .front-role {
    position: absolute; left: 0; right: 0; top: 230px;
    font-size: 15px; font-weight: 700; color: var(--gold-light);
  }
  .front-rule {
    position: absolute; left: 132px; width: 276px; top: 252px;
    height: 1px; background: var(--gold);
  }
  .front-technique {
    position: absolute; left: 0; right: 0; top: 256px;
    font-size: 12.5px; font-weight: 600; color: var(--gold-light);
  }

  .card-back { top: 568px; display: flex; }
  .back-brand {
    position: relative; width: 254px; height: 100%;
    background: var(--paper); color: var(--gold-print);
  }
  .back-brand .brow-art { left: 30px; top: 76px; width: 192px; height: 54px; transform: rotate(-6deg); }
  .back-name {
    position: absolute; left: 30px; top: 136px;
    font-size: 31px; font-weight: 700; line-height: 1;
  }
  .back-role {
    position: absolute; left: 30px; top: 172px;
    font-size: 10.5px; font-weight: 700;
  }
  .back-person {
    position: absolute; right: 32px; top: 230px;
    font-size: 15px; font-weight: 700;
  }
  .back-contact {
    flex: 1;
    background: linear-gradient(160deg, var(--choc-light) 0%, var(--choc) 50%, var(--choc-dark) 100%);
    color: var(--gold-print);
    padding: 110px 0 0 28px;
    font-size: 13.5px; line-height: 19px;
  }
  .back-contact address { font-style: normal; }
  .back-contact .phone { margin-top: 9px; }
  .back-contact .web { margin-top: 6px; }
</style>
</head>
<body>
<main class="canvas">
  <section class="card card-front">
    <div class="brow-art" role="img" aria-label="Gold feathered eyebrow illustration drawn in fine hair strokes"></div>
    <h1 class="front-name">Glint Lashline</h1>
    <p class="front-role">Tessa, brow specialist and cosmetic tattooist</p>
    <div class="front-rule"></div>
    <p class="front-technique">using feathered and hairstroke techniques</p>
  </section>

  <section class="card card-back">
    <div class="back-brand">
      <div class="brow-art" role="img" aria-label="Gold feathered eyebrow illustration drawn in fine hair strokes"></div>
      <h2 class="back-name">Glint Lashline</h2>
      <p class="back-role">brow specialist and cosmetic tattooist</p>
      <p class="back-person">Tessa</p>
    </div>
    <div class="back-contact">
      <address>
        Serene Glow Spa &amp; Skin Studio<br>
        Shop 42, Hollin Park Market Arcade<br>
        Tamsworth-Delby Parade<br>
        Kelford Downs<br>
        Vic 3917.
      </address>
      <p class="phone">03 5126-4730</p>
      <p class="web">www.glintlashline.com.au</p>
    </div>
  </section>
</main>
</body>
</html>
```